BRISK is looking for a design partner

We are a group of videographers, photographers and editors currently rebranding our company. Originally Marco Lenhill Photography, we have grown over the years into a company that does a lot of different things for a variety of corporate clients. It's clear the company is no longer Marco, but a whole team. We have submitted a design contest for our new logo, purchased our new URL/email, and are now looking to get things moving on the website. We have most copy ready and are looking to help move online. The site should load quickly, be mobile friendly, look modern, and be very easy to navigate. Our videos run on Flickcast so we need to make sure that we can embed or run videos from the Flickcast account.

We are excited to be starting this new chapter. Hopefully you can come along with us! Marco

Target Market(s)

Businesses looking to see what we do, examples of our work, and who we are.

Industry/Entity Type

Multimedia

Font styles to use
Serif
Sans Serif

Colors
33a6d7
3176b5
ffffff

Requirements
Must have
• I believe we are looking for a bright white background website.

Here is a list of areas that we will need to have on the site.
-Overview video near top
-Our Mission
-Details of services
-About the team
-Our History (3 sections: Different from Start, Growth, Transformation)
-Working at BRISK (area for talent and freelancer to see employment info, current opening, how to apply
-Internship Program details
-Contact Form
-FAQ
Nice to have
• Social media links, slideshow, etc
We need photo and videos sprinkled throughout the site to give it as modern a look as possible. I am open to using this for backgrounds or to segment sections. See our current site here marcolenhillphotography.example/business/
Should not have
• Cannot load slow. This is our current challenge. Any thing we can do to move this along will be helpful.

```html
<!DOCTYPE html>
<html lang="en">
<head>
<meta charset="utf-8">
<title>Marco Lenhill Films &amp; Photography</title>
<link href="https://fonts.googleapis.com/css2?family=Barlow:wght@400;500;600;700;800&family=Lora:ital@1&display=swap" rel="stylesheet">
<style>
:root{
  --blue:#33a6d7;
  --blue-deep:#3176b5;
  --blue-bright:#0aa3ea;
  --ink:#1b1b1b;
  --text:#555;
  --muted:#999;
  --night:#0b0e14;
  --soft:#f6f6f6;
  --white:#fff;
}
*{margin:0;padding:0;box-sizing:border-box}
html,body{width:1200px;height:4000px;overflow:hidden;background:var(--white)}
body{font-family:"Barlow",sans-serif;color:var(--text);position:relative}
.abs{position:absolute}
.ph{position:absolute}

/* header */
.site-header{position:absolute;left:0;top:0;width:1200px;height:73px;background:var(--white);z-index:5}
.brand{position:absolute;left:158px;top:18px;display:flex;align-items:center;gap:8px}
.brand-dot{width:22px;height:22px;border-radius:50%;background:var(--blue-bright)}
.brand-name{font-family:"Lora",serif;font-style:italic;font-size:22px;color:var(--blue-bright);line-height:1}
.brand-sub{font-size:8px;letter-spacing:1px;color:var(--blue-bright);margin-top:2px}
.nav{position:absolute;left:405px;top:32px;display:flex;gap:16px;font-size:14px;color:var(--ink)}
.nav .active{color:var(--blue-bright)}
.btn-quote{position:absolute;left:887px;top:26px;width:158px;height:32px;border-radius:16px;background:var(--blue-bright);color:#fff;font-size:13px;font-weight:600;letter-spacing:.5px;text-align:center;line-height:32px}

/* hero */
.hero-photo{left:0;top:73px;width:1200px;height:560px;background:linear-gradient(120deg,#2a2f36 0%,#14171c 45%,#3a3f45 70%,#101216 100%)}
.hero-kicker{left:154px;top:224px;font-size:27px;font-weight:700;color:var(--blue-bright)}
.hero-title{left:154px;top:276px;font-size:41px;font-weight:800;color:#fff;letter-spacing:.5px}
.hero-bar{left:0;top:312px;width:640px;height:7px;background:var(--blue-bright)}
.hero-copy{left:156px;top:346px;width:480px;font-size:13.5px;line-height:24px;color:#fff}
.bracket-btn{left:156px;top:451px;width:122px;height:42px;color:var(--blue-bright);font-size:14px;font-weight:600;text-align:center;line-height:42px}
.bracket-btn::before,.bracket-btn::after{content:"";position:absolute;top:0;width:10px;height:42px;border:2px solid #fff}
.bracket-btn::before{left:0;border-right:none}
.bracket-btn::after{right:0;border-left:none}
.play{left:821px;top:297px;width:76px;height:76px;border-radius:50%;border:2px solid #fff;display:flex;align-items:center;justify-content:center}
.play span{width:58px;height:58px;border-radius:50%;background:var(--blue-bright);display:flex;align-items:center;justify-content:center}
.play-label{left:820px;top:384px;width:80px;text-align:center;font-size:9px;font-weight:700;color:#fff}

/* section titles */
.sec-title{position:absolute;font-size:27px;font-weight:800;color:var(--ink);letter-spacing:.3px;padding:0 14px;line-height:1}
.sec-title b{position:relative;z-index:1;font-weight:800}
.sec-title i{position:absolute;left:14px;right:14px;bottom:-4px;height:7px;background:var(--blue-bright)}
.sec-title::before,.sec-title::after{content:"";position:absolute;top:-14px;width:8px;height:8px;border-top:2px solid var(--blue-bright)}
.sec-title::before{left:0;border-left:2px solid var(--blue-bright)}
.sec-title::after{right:0;border-right:2px solid var(--blue-bright)}
.on-dark{color:#fff}
.center{left:0;right:0;margin:auto;width:max-content}

/* mission */
.mission-copy{left:154px;top:732px;width:446px;font-size:12.5px;line-height:24.8px;color:var(--text)}
.btn-film{left:900px;top:681px;width:150px;height:43px;background:var(--blue-bright);color:#fff;font-size:14px;font-weight:600;display:flex;align-items:center;justify-content:center;gap:8px}
.photo-frame{border:8px solid #fff;box-shadow:0 6px 24px rgba(0,0,0,.1)}
.mark-circle{left:857px;top:828px;width:54px;height:54px;border-radius:50%;background:#fff;box-shadow:0 3px 12px rgba(0,0,0,.15);display:flex;align-items:center;justify-content:center}
.mark-circle span{width:22px;height:22px;border-radius:50%;background:var(--blue-bright)}

/* video services */
.service{position:absolute;width:280px;color:#fff}
.service h3{display:flex;align-items:center;gap:12px;font-size:16px;font-weight:700;margin-bottom:16px}
.service p{font-size:12.5px;line-height:21px}

/* photography */
.photo-item{position:absolute;left:460px;width:580px}
.ps-icon{position:absolute;left:0;top:0;width:62px;height:54px;border-radius:4px;background:var(--blue-bright);box-shadow:0 4px 10px rgba(10,163,234,.35);display:flex;align-items:center;justify-content:center}
.photo-item h4{margin-left:78px;font-size:13px;font-weight:600;color:var(--ink);margin-bottom:8px}
.photo-item p{margin-left:78px;font-size:12.5px;line-height:24px;color:var(--text)}

/* history */
.history-band{left:0;top:2452px;width:1200px;height:456px;background:var(--soft)}
.sub{position:absolute;font-size:13px;color:var(--text);text-align:center;line-height:24px}
.step{position:absolute;width:260px;text-align:center}
.step-ring{width:112px;height:112px;margin:0 auto;border-radius:50%;border:3px solid var(--blue-deep);padding:4px}
.step-ring span{display:flex;width:100%;height:100%;border-radius:50%;background:linear-gradient(160deg,var(--blue-bright),var(--blue-deep));align-items:center;justify-content:center}
.step-no{margin-top:15px;font-size:13px;color:var(--muted)}
.step h5{margin-top:6px;font-size:19px;font-weight:700;color:var(--blue-deep);letter-spacing:.5px}
.step p{margin-top:10px;font-size:11.5px;line-height:20px;color:var(--muted)}
.step-arrow{position:absolute;top:2666px;width:135px;border-top:1px dashed #aaa}
.step-arrow::after{content:"";position:absolute;right:0;top:-4px;width:6px;height:6px;border-top:1px solid #888;border-right:1px solid #888;transform:rotate(45deg)}

/* team */
.member{position:absolute;width:187px;text-align:center}
.member .pic{width:187px;height:195px;border-radius:26px}
.member h6{margin-top:14px;font-size:16px;font-weight:500;color:var(--ink)}
.member small{display:block;margin-top:4px;font-size:11.5px;color:var(--muted)}

/* working */
.tab{position:absolute;width:240px;text-align:center}
.tab strong{display:block;font-size:19px;font-weight:600;color:#8a8a8a}
.tab.on strong{color:var(--blue-bright)}
.tab em{display:block;font-style:normal;font-size:13px;color:var(--muted);margin-top:10px}
.tab.on em{color:var(--ink)}
.perk{position:absolute;left:380px;width:470px}
.perk small{font-size:12px;color:#f07c2a}
.perk h6{font-size:15px;font-weight:500;color:var(--ink);margin:6px 0 8px}
.perk p{font-size:13px;line-height:24px;color:var(--text)}
.perk-card{left:130px;top:3872px;width:940px;height:140px;background:#fff;box-shadow:0 0 28px rgba(0,0,0,.07)}
.btn-more{left:902px;top:3939px;width:110px;height:34px;border:1px solid var(--blue-bright);border-radius:17px;color:var(--blue-bright);font-size:11px;font-weight:600;text-align:center;line-height:32px}
</style>
</head>
<body>

<header class="site-header">
  <div class="brand">
    <div class="brand-dot"></div>
    <div><div class="brand-name">Marco Lenhill</div><div class="brand-sub">FILMS AND PHOTOGRAPHY</div></div>
  </div>
  <nav class="nav"><span class="active">Home</span><span>Services</span><span>Portfolio</span><span>Clients</span><span>About</span><span>Contact</span><span>FAQ</span></nav>
  <div class="btn-quote">REQUEST A QUOTE</div>
</header>

<!-- hero -->
<div class="ph hero-photo" role="img" aria-label="Videographer holding a cinema camera in a city street at dusk"></div>
<div class="abs hero-kicker">Marco Lenhill</div>
<div class="abs hero-bar"></div>
<div class="abs hero-title">FILMS &amp; PHOTOGRAPHY</div>
<p class="abs hero-copy">There are many variations of passages of Lorem Ipsum available, but the majority have suffered alteration. There are many variations of passages of Lorem Ipsum avaiable, but the majority have suffered alteration</p>
<div class="abs bracket-btn">LEARN MORE</div>
<div class="abs play"><span><svg width="16" height="16" viewBox="0 0 16 16"><path d="M5 3l8 5-8 5z" fill="#fff"/></svg></span></div>
<div class="abs play-label">PLAY VIDEO</div>
<svg class="abs" style="left:0;top:560px" width="1200" height="90" viewBox="0 0 1200 90">
  <path d="M0 53 L210 8 L680 60 L1200 26 L1200 90 L0 90Z" fill="#fff"/>
  <path d="M0 53 L0 63 L210 20 L680 68 L1200 45 L1200 26 L680 55 L210 8Z" fill="var(--blue-bright)"/>
</svg>

<!-- mission -->
<h2 class="sec-title" style="left:154px;top:683px"><b>OUR MISSION</b><i></i></h2>
<p class="abs mission-copy">Many business and organizations are overwhelmed and struggle to deliver high quality content that speaks to their brand, connects with their customers, and produces results. Our TEAM helps our clients identify their story. We then guide and create beautiful content to communicate their story in variety of video formats. + A reputation for award winning content. With over 1000 videos produced in the last five years clients have complete confidence we deliver. The proof is in our product. High quality award winning storytelling and content. It's who we are. + We listen. You may not know how to tell your story… but you know your brand, your goals, your assets, what makes your company awesome. We absorb all of that and create a plan and content unique to you, your business and your goals. + The experience matters. It is not enough just to make great content.</p>
<div class="ph" style="left:650px;top:680px;width:225px;height:285px;background:linear-gradient(160deg,#6b4a3a,#2c1d17)" role="img" aria-label="Portrait of a woman with warm studio light"></div>
<div class="abs btn-film"><svg width="16" height="16" viewBox="0 0 16 16"><circle cx="8" cy="8" r="7" fill="none" stroke="#fff" stroke-width="1.4"/><path d="M6.5 5l4 3-4 3z" fill="#fff"/></svg>View Film</div>
<div class="ph" style="left:886px;top:750px;width:226px;height:286px;background:linear-gradient(150deg,#2c5bd8,#5a1f7a 60%,#d8386a)" role="img" aria-label="Profile of a woman lit in blue and magenta light"></div>
<div class="ph photo-frame" style="left:687px;top:853px;width:228px;height:245px;background:linear-gradient(180deg,#f3e4e3,#d7b4b0 70%,#6b5550)" role="img" aria-label="Photographer crouching with a camera on a rock"></div>
<div class="abs mark-circle"><span></span></div>
<svg class="abs" style="left:985px;top:950px" width="160" height="115">
  <g fill="#c5c9d0">
    <circle cx="148" cy="2" r="1.5"/><circle cx="148" cy="17" r="1.5"/><circle cx="148" cy="32" r="1.5"/><circle cx="148" cy="47" r="1.5"/><circle cx="148" cy="62" r="1.5"/><circle cx="148" cy="77" r="1.5"/><circle cx="133" cy="2" r="1.5"/><circle cx="133" cy="17" r="1.5"/><circle cx="133" cy="32" r="1.5"/><circle cx="133" cy="47" r="1.5"/><circle cx="133" cy="62" r="1.5"/><circle cx="133" cy="77" r="1.5"/>
    <circle cx="5" cy="97" r="1.5"/><circle cx="20" cy="97" r="1.5"/><circle cx="35" cy="97" r="1.5"/><circle cx="50" cy="97" r="1.5"/><circle cx="65" cy="97" r="1.5"/><circle cx="80" cy="97" r="1.5"/><circle cx="95" cy="97" r="1.5"/><circle cx="110" cy="97" r="1.5"/><circle cx="125" cy="97" r="1.5"/><circle cx="140" cy="97" r="1.5"/>
    <circle cx="5" cy="110" r="1.5"/><circle cx="20" cy="110" r="1.5"/><circle cx="35" cy="110" r="1.5"/><circle cx="50" cy="110" r="1.5"/><circle cx="65" cy="110" r="1.5"/><circle cx="80" cy="110" r="1.5"/><circle cx="95" cy="110" r="1.5"/><circle cx="110" cy="110" r="1.5"/><circle cx="125" cy="110" r="1.5"/><circle cx="140" cy="110" r="1.5"/>
  </g>
</svg>

<!-- video services -->
<svg class="abs" style="left:0;top:1140px" width="1200" height="640" viewBox="0 0 1200 640">
  <path d="M0 12 L210 60 L680 4 L1200 42 L1200 595 L680 630 L210 580 L0 630Z" fill="var(--night)"/>
  <path d="M0 0 L210 50 L680 0 L1200 35 L1200 50 L680 16 L210 66 L0 20Z" fill="var(--blue-bright)"/>
  <path d="M0 620 L210 570 L680 625 L1200 590 L1200 606 L680 640 L210 588 L0 640Z" fill="var(--blue-bright)"/>
</svg>
<div class="ph" style="left:440px;top:1360px;width:330px;height:360px;background:radial-gradient(ellipse at 50% 45%,#5a4a3c,#1b1712 70%,rgba(11,14,20,0))" role="img" aria-label="Cameraman holding a cinema camera toward the viewer"></div>
<h2 class="sec-title on-dark center" style="top:1228px"><b>VIDEO SERVICES</b><i></i></h2>
<div class="service" style="left:156px;top:1312px">
  <h3><svg width="32" height="26" viewBox="0 0 32 26"><circle cx="7" cy="6" r="5" fill="var(--blue-bright)"/><circle cx="18" cy="6" r="5" fill="var(--blue-bright)"/><rect x="1" y="12" width="22" height="13" rx="2" fill="var(--blue-bright)"/><path d="M24 16l7-4v13l-7-4z" fill="var(--blue-bright)"/></svg>Professional Video Production</h3>
  <p>Professional Video Production Today, more than ever, video is helping you reach your target audience. From Friendwall feeds to viral Streamtube videos, great content is going further.</p>
</div>
<div class="service" style="left:778px;top:1320px">
  <h3><svg width="32" height="32" viewBox="0 0 32 32"><circle cx="16" cy="16" r="14" fill="var(--blue-bright)"/><g fill="var(--night)"><circle cx="16" cy="8" r="3.5"/><circle cx="16" cy="24" r="3.5"/><circle cx="8" cy="16" r="3.5"/><circle cx="24" cy="16" r="3.5"/></g></svg>Sizzle Reels</h3>
  <p>Professional Video Production Today, more than ever, video is helping you reach your target audience. From Friendwall feeds to viral Streamtube videos, great content is going further.</p>
</div>
<div class="service" style="left:156px;top:1496px">
  <h3><svg width="34" height="34" viewBox="0 0 34 34"><circle cx="17" cy="17" r="15" fill="var(--blue-bright)"/><circle cx="17" cy="17" r="5" fill="var(--night)"/><path d="M17 2v10M32 17H22M17 32V22M2 17h10" stroke="var(--night)" stroke-width="2"/></svg>Raw Services</h3>
  <p>Many out of town businesses we serve need elements such as interviews or broll provided for projects. Instead of incurring travel, production, and logistics costs, we take care of everything.</p>
</div>
<div class="service" style="left:778px;top:1500px">
  <h3><svg width="30" height="34" viewBox="0 0 30 34"><circle cx="15" cy="8" r="2.5" fill="var(--blue-bright)"/><path d="M9 3a8 8 0 000 10M21 3a8 8 0 010 10" stroke="var(--blue-bright)" stroke-width="2" fill="none"/><rect x="1" y="18" width="28" height="14" fill="none" stroke="var(--blue-bright)" stroke-width="2"/><text x="15" y="29" text-anchor="middle" font-family="Barlow,sans-serif" font-size="10" font-weight="700" fill="var(--blue-bright)">LIVE</text></svg>Live Broadcast</h3>
  <p>Many out of town businesses we serve need elements such as interviews or broll provided for projects. Instead of incurring travel, production, and logistics costs, we take care of everything.</p>
</div>

<!-- photography services -->
<h2 class="sec-title center" style="top:1840px"><b>PHOTOGRAPHY SERVICES</b><i></i></h2>
<div class="ph" style="left:156px;top:1924px;width:268px;height:240px;background:radial-gradient(circle at 30% 40%,#c58a3a,#4a2a14 60%,#1c120a)" role="img" aria-label="Child watching sparklers at an evening event"></div>
<div class="ph" style="left:156px;top:2182px;width:268px;height:218px;background:linear-gradient(120deg,#ff6a1a,#f98c3a 55%,#f3b37a)" role="img" aria-label="Smiling baby against an orange backdrop"></div>
<div class="photo-item" style="top:1924px">
  <div class="ps-icon"><svg width="28" height="28" viewBox="0 0 28 28" fill="none" stroke="#fff" stroke-width="1.6"><rect x="3" y="12" width="22" height="13" rx="1"/><circle cx="9" cy="6" r="3"/><circle cx="19" cy="6" r="3"/><path d="M7 18h14M7 21h10"/></svg></div>
  <h4>Event Photography</h4>
  <p>From small company meetings to 15,000+ tech conferences, LHP can capture your moment. Our professional team has the experience to not only give you great images but a great experience.</p>
</div>
<div class="photo-item" style="top:2047px">
  <div class="ps-icon"><svg width="28" height="28" viewBox="0 0 28 28" fill="none" stroke="#fff" stroke-width="1.6"><rect x="4" y="4" width="18" height="16" rx="2" transform="rotate(-8 13 12)"/><rect x="8" y="9" width="16" height="14" rx="2"/><circle cx="16" cy="16" r="3"/></svg></div>
  <h4>Interactive Photography (photobooth)</h4>
  <p>Over the years we have pioneered innovative concepts to help you broaden your reach. Our photo booths not only offer branded prints but the ability for guests to text and email their images instantly.</p>
</div>
<div class="photo-item" style="top:2170px">
  <div class="ps-icon"><svg width="28" height="28" viewBox="0 0 28 28" fill="none" stroke="#fff" stroke-width="1.6"><path d="M3 8V3h5M20 3h5v5M25 20v5h-5M8 25H3v-5"/><circle cx="14" cy="11" r="4"/><path d="M7 23c1-5 4-7 7-7s6 2 7 7"/></svg></div>
  <h4>Headshots &amp; Corporate Photography</h4>
  <p>From small company meetings to 15,000+ tech conferences, LHP can capture your moment. Our professional team has the experience to not only give you great images but a great experience.</p>
</div>
<div class="photo-item" style="top:2292px">
  <div class="ps-icon"><svg width="28" height="28" viewBox="0 0 28 28" fill="none" stroke="#fff" stroke-width="1.6"><rect x="3" y="6" width="22" height="17" rx="3"/><circle cx="14" cy="14.5" r="4.5"/><path d="M6 10h3"/></svg></div>
  <h4>SnapBooth</h4>
  <p>In 2016 LHP launched SnapBooth, our innovate solution to step and repeat backdrops. We noticed a lot of people take photos at these branded backdrops. However the photos never seam to find their way to the people in the photos.</p>
</div>

<!-- history -->
<div class="abs history-band"></div>
<div class="ph" style="left:0;top:2580px;width:340px;height:328px;background:radial-gradient(circle at 40% 45%,#e2e2e2,#efefef 60%,rgba(246,246,246,0))" role="img" aria-label="Faint backdrop of a photographer with a camera"></div>
<div class="abs" style="left:1160px;top:2568px;width:84px;height:84px;border-radius:50%;background:#dceff9"></div>
<div class="abs" style="left:1098px;top:2712px;width:82px;height:82px;border-radius:50%;background:#dceff9"></div>
<h2 class="sec-title center" style="top:2492px"><b>OUT HISTORY</b><i></i></h2>
<p class="sub" style="left:0;width:1200px;top:2542px">BRISK is the product of more than a decade of forward thinking, evolution, transformation.</p>
<div class="step" style="left:166px;top:2612px">
  <div class="step-ring"><span><svg width="48" height="48" viewBox="0 0 48 48" fill="none" stroke="#fff" stroke-width="2"><path d="M24 26V12M24 16c-4-6-10-4-10-4s0 8 10 6M24 14c4-6 10-4 10-4s0 8-10 6"/><path d="M6 28l8 12h20l8-12-8 4-6-2H20l-6 2z"/></svg></span></div>
  <div class="step-no">Step 1</div><h5>START</h5>
  <p>We got our start in 2008 by Marco Lenhill who envisioned turning a photography hobby into a small business.</p>
</div>
<div class="step" style="left:468px;top:2612px">
  <div class="step-ring"><span><svg width="48" height="48" viewBox="0 0 48 48" fill="none" stroke="#fff" stroke-width="2"><path d="M8 40h32M14 40V30M24 40V24M34 40V16M12 28l10-8 8 4 12-12M36 12h6v6"/></svg></span></div>
  <div class="step-no">Step 2</div><h5>GROWTH</h5>
  <p>Within a few years the company evolved into video work. This may have been inevitable given Marco's</p>
</div>
<div class="step" style="left:771px;top:2612px">
  <div class="step-ring"><span><svg width="48" height="48" viewBox="0 0 48 48" fill="none" stroke="#fff" stroke-width="2"><path d="M24 42V26M18 40h12M24 30c-8 0-14-4-14-11 0-5 4-9 9-9 1-3 3-4 5-4s4 1 5 4c5 0 9 4 9 9 0 7-6 11-14 11z"/></svg></span></div>
  <div class="step-no">Step 3</div><h5>TRANSFORMATION</h5>
  <p>To meet increasing demand, many of our talented freelancers became employees. Eventually</p>
</div>
<div class="step-arrow" style="left:381px"></div>
<div class="step-arrow" style="left:684px"></div>

<!-- team -->
<div class="abs" style="left:126px;top:2960px;width:130px;height:96px;border-radius:60% 40% 55% 45%;background:#e3f1fa;transform:rotate(-18deg)"></div>
<div class="abs" style="left:966px;top:2983px;width:30px;height:30px;border-radius:50%;background:#dceff9"></div>
<div class="abs" style="left:920px;top:3070px;width:160px;height:160px;border-radius:50%;background:#e3f1fa"></div>
<h2 class="sec-title center" style="top:2972px"><b>ABOUT THE TEAM</b><i></i></h2>
<p class="sub" style="left:0;width:1200px;top:3030px">If it is affordability and security of a mid-sized community with the&nbsp; business and career<br>opportunities of a big city that you're looking for</p>
<div class="member" style="left:160px;top:3131px">
  <div class="pic" style="background:linear-gradient(160deg,#4db8ea,#2a8fcf)" role="img" aria-label="Team member holding a camera, blue overlay"></div>
  <h6>Owen Hartley</h6><small>Founder, Framewell</small>
</div>
<div class="member" style="left:395px;top:3124px">
  <div class="pic" style="background:linear-gradient(160deg,#d9d3cc,#8b6a58)" role="img" aria-label="Portrait of a team member"></div>
  <h6>Lena Marsh</h6><small>Founder, Framewell</small>
</div>
<div class="member" style="left:621px;top:3131px">
  <div class="pic" style="background:linear-gradient(160deg,#e6e6e6,#5a5f66)" role="img" aria-label="Editor working at a computer desk"></div>
  <h6>Tobias Reyes</h6><small>Founder, Framewell</small>
</div>
<div class="member" style="left:851px;top:3116px">
  <div class="pic" style="background:linear-gradient(160deg,#cfdbe4,#3a3a40)" role="img" aria-label="Smiling photographer holding a camera"></div>
  <h6>Nina Castell</h6><small>Founder, Framewell</small>
</div>

<!-- working -->
<h2 class="sec-title center" style="top:3458px"><b>WORKING AT BRISK</b><i></i></h2>
<p class="sub" style="left:0;width:1200px;top:3516px">Our team is made up of some of the greatest people on earth… who happen to be talented too.<br>We are strong believers that our people are the difference between mundane and awesome content.&nbsp; If you<br>are committed to learning, supporting, and helping those around you we want to hear from you.</p>
<div class="tab on" style="left:169px;top:3625px"><strong>Full time jobs</strong><em>November 10, 2018</em></div>
<div class="tab" style="left:486px;top:3625px"><strong>Freelance partners</strong><em>November 10, 2018</em></div>
<div class="tab" style="left:782px;top:3625px"><strong>How to apply</strong><em>Click here to apply</em></div>
<div class="abs" style="left:142px;top:3700px;width:924px;height:2px;background:#ddd"></div>
<div class="abs" style="left:142px;top:3699px;width:293px;height:4px;background:var(--blue-bright)"></div>
<div class="ph" style="left:220px;top:3738px;width:112px;height:102px;border-radius:18px;background:linear-gradient(160deg,#d9d9d9,#a64a3a)" role="img" aria-label="Portrait of a staff member"></div>
<div class="perk" style="top:3742px">
  <small>Owen Hartley</small><h6>Livable wages</h6>
  <p>If it is affordability and security of a mid-sized community with the<br>business and career opportunities of a big city that you're looking for</p>
</div>
<div class="abs perk-card"></div>
<div class="ph" style="left:227px;top:3888px;width:112px;height:102px;border-radius:18px;background:linear-gradient(160deg,#2b4b8a,#c7532e)" role="img" aria-label="Portrait of a staff member at an event"></div>
<div class="perk" style="top:3894px">
  <small>Peter Vale</small><h6>Health, Dental and Vision Insurance</h6>
  <p>If it is affordability and security of a mid-sized community&nbsp; with the<br>business and career opportunities of a big city that you're looking for</p>
</div>
<div class="abs btn-more">READ MORE</div>

</body>
</html>
```